Design for a 3-4 screens mobile app

The app is a "simple" ordering mobile app.
1. START screen : user can select either "NEW order" either "VIEW history" - or, can access the usual Contact, About, and Conditions pages.
2. NEW order : is a sequence of 3 basic screens/forms made of 3-4 fields each. Logic is the following: you select the service you need, its recurrence, mention where you are located and then you post it towards the marketplace...
3. VIEW history : is where you land at the end of the ordering process - and accessible from START screen. You see there your previous orders, and their statuses.
Mandatory : we need design for START screen, NEW order and VIEW history screens.
Design but be optimized for Smartphones, used in Portrait mode.
Please take into account the design of the website promoting the Mobile App: https://quikpadvora.be/
Optional but of course nice to have if you could propose some design or guidance for Contact, About, and Conditions pages...
Here attached a full screen sequence.
Updates
Thanks for all your proposals ! They were submitted to the final customer, he selects one ASAP !
Number of Pages Required
3 page
Look and feel
Each slider illustrates characteristics of the customer's brand and the style your logo design should communicate.

```html
<!DOCTYPE html>
<html lang="en">
<head>
<meta charset="utf-8">
<title>Quikpad Vora – Start</title>
<link href="https://fonts.googleapis.com/css2?family=Roboto+Condensed:wght@400;700&family=Arimo:wght@400&display=swap" rel="stylesheet">
<style>
  :root {
    --orange: #ff6600;
    --orange-light: #ff9933;
    --logo-yellow: #ffd24a;
    --teal: #00b597;
    --white: #ffffff;
    --ink: #2b2b2b;
    --button-dark: #222222;
    --footer: #333333;
    --footer-line: #555555;
    --footer-text: #f0f0f0;
  }
  * { box-sizing: border-box; margin: 0; padding: 0; }
  html, body { width: 1200px; height: 2161px; overflow: hidden; background: var(--white); }
  body { font-family: "Roboto Condensed", sans-serif; }

  .app { width: 1200px; height: 2161px; display: flex; flex-direction: column; }

  .brand-bar {
    height: 304px; flex: none; background: var(--orange);
    display: flex; align-items: center; justify-content: center; gap: 30px;
  }
  .brand-mark {
    width: 170px; height: 170px; border-radius: 50%;
    background: radial-gradient(circle at 50% 40%, #f3a65a, #d9822f);
  }
  .brand-name { color: var(--logo-yellow); font-weight: 700; font-size: 80px; letter-spacing: -0.5px; }

  .tool-bar {
    height: 117px; flex: none; background: var(--orange-light);
    display: flex; align-items: center; justify-content: space-between;
    padding: 0 38px;
  }
  .tool-button {
    width: 96px; height: 90px; background: var(--button-dark); border-radius: 6px;
    display: flex; align-items: center; justify-content: center;
    color: var(--white); text-decoration: none;
  }
  .menu-button { width: 102px; }
  .network-name { font-weight: 700; font-size: 30px; }
  .share-group { display: flex; gap: 6px; }

  .welcome {
    height: 437px; flex: none; background: var(--teal); color: var(--white);
    text-align: center; font-size: 37px; padding-top: 50px;
  }
  .welcome-intro { line-height: 45px; padding: 0 30px; }
  .contact-list { list-style: none; margin-top: 26px; }
  .contact-item {
    display: flex; align-items: center; justify-content: center; gap: 24px;
    height: 80px;
  }
  .contact-item svg { width: 48px; height: 48px; }

  .actions { flex: 1; display: flex; flex-direction: column; align-items: center; padding-top: 88px; }
  .action { display: flex; flex-direction: column; align-items: center; text-decoration: none; }
  .action-label { color: var(--orange); font-weight: 700; font-size: 62px; line-height: 62px; }
  .action-new svg { width: 262px; height: 262px; }
  .action-new .action-label { margin-top: 56px; }
  .action-history { margin-top: 99px; }
  .action-history svg { width: 280px; height: 280px; }
  .action-history .action-label { margin-top: 49px; }

  .footer-nav {
    height: 119px; flex: none; background: var(--footer); border-bottom: 2px solid var(--footer-line);
    display: flex; align-items: center; justify-content: center;
    font-family: "Arimo", sans-serif; font-size: 31px;
  }
  .footer-nav a { color: var(--footer-text); text-decoration: none; padding: 0 36px; }
  .footer-nav a + a { border-left: 2px solid var(--footer-line); }
  .copyright {
    height: 117px; flex: none; background: var(--footer); color: var(--footer-text);
    display: flex; align-items: center; justify-content: center;
    font-family: "Arimo", sans-serif; font-size: 28px;
  }
</style>
</head>
<body>
<div class="app">
  <header class="brand-bar">
    <div class="brand-mark" role="img" aria-label="Brand illustration: cleaning helper with a broom"></div>
    <span class="brand-name">Quikpad Vora</span>
  </header>

  <nav class="tool-bar">
    <a class="tool-button menu-button" href="#" aria-label="Menu">
      <svg width="56" height="44" viewBox="0 0 56 44"><g fill="#fff"><rect y="2" width="56" height="7" rx="2"/><rect y="18" width="56" height="7" rx="2"/><rect y="34" width="56" height="7" rx="2"/></g></svg>
    </a>
    <div class="share-group">
      <a class="tool-button" href="#"><span class="network-name">Pelo</span></a>
      <a class="tool-button" href="#"><span class="network-name">Viru</span></a>
      <a class="tool-button" href="#" aria-label="Call">
        <svg width="46" height="46" viewBox="0 0 24 24"><path fill="#fff" d="M6.6 10.8c1.4 2.8 3.8 5.1 6.6 6.6l2.2-2.2c.3-.3.7-.4 1-.2 1.1.4 2.3.6 3.6.6.6 0 1 .4 1 1V20c0 .6-.4 1-1 1C10.6 21 3 13.4 3 4c0-.6.4-1 1-1h3.5c.6 0 1 .4 1 1 0 1.3.2 2.5.6 3.6.1.3 0 .7-.2 1z"/></svg>
      </a>
      <a class="tool-button" href="#" aria-label="Email">
        <svg width="60" height="44" viewBox="0 0 60 44"><rect x="3" y="3" width="54" height="38" fill="none" stroke="#fff" stroke-width="5"/><path d="M4 5 L30 26 L56 5" fill="none" stroke="#fff" stroke-width="5"/></svg>
      </a>
    </div>
  </nav>

  <section class="welcome">
    <p class="welcome-intro">Welcome on Quikpad Vora, should you have any question about this App or our services, do not hesitate to</p>
    <ul class="contact-list">
      <li class="contact-item">
        <svg viewBox="0 0 48 48"><circle cx="24" cy="24" r="21" fill="none" stroke="#fff" stroke-width="3"/><path d="M18 14c-2 2-3 5 0 10s7 9 11 10c2 .5 4-1 4-2l-4-4-2 2c-2-1-5-4-6-6l2-2-4-4z" fill="none" stroke="#fff" stroke-width="2.5" stroke-linejoin="round"/></svg>
        <span>Call us on +32 470 55 21 09</span>
      </li>
      <li class="contact-item">
        <svg viewBox="0 0 48 48"><rect x="3" y="10" width="42" height="28" fill="none" stroke="#fff" stroke-width="3"/><path d="M4 11 L24 27 L44 11" fill="none" stroke="#fff" stroke-width="3"/></svg>
        <span>Email at info@quikpadvora.be</span>
      </li>
      <li class="contact-item">
        <svg viewBox="0 0 48 48"><g fill="none" stroke="#fff" stroke-width="3"><circle cx="24" cy="24" r="20"/><ellipse cx="24" cy="24" rx="9" ry="20"/><path d="M4 24h40M7 14h34M7 34h34M24 4v40"/></g></svg>
        <span>Visit our Website at quikpadvora.be</span>
      </li>
    </ul>
  </section>

  <main class="actions">
    <a class="action action-new" href="#">
      <svg viewBox="0 0 280 280"><g fill="none" stroke="var(--ink)" stroke-width="10" stroke-linecap="round"><circle cx="140" cy="140" r="130"/><path d="M140 60v160M60 140h160"/></g></svg>
      <span class="action-label">New Order</span>
    </a>
    <a class="action action-history" href="#">
      <svg viewBox="0 0 290 290"><g fill="none" stroke="var(--ink)" stroke-width="9" stroke-linecap="round" stroke-linejoin="round">
        <path d="M160 282H40a12 12 0 0 1-12-12V20A12 12 0 0 1 40 8h220a12 12 0 0 1 12 12v130"/>
        <path d="M10 58h36M10 126h36M10 194h36M10 262h36"/>
        <path d="M96 70h130M96 106h130M96 150h60M96 196h20M96 240h20"/>
        <circle cx="212" cy="222" r="62"/><path d="M212 186v40h28"/>
      </g></svg>
      <span class="action-label">View History</span>
    </a>
  </main>

  <nav class="footer-nav">
    <a href="#">About</a><a href="#">Contact</a><a href="#">Terms of Use</a>
  </nav>
  <footer class="copyright">© Copyright 2017 Quikpad Vora. All Rights Reserved.</footer>
</div>
</body>
</html>
```